Homepage Redesign - Hi-tech business Law Firm

I'm looking for an updated graphic design (pdf file) for the homepage of dorvantlegal.ca (and which will form the general template of the other pages - but you don't need to design that). Detailed specs are in the Word file.

Deliverable is 1 pdf file that I find good looking, that sets forth the layout of the new page.

Target Market(s)

Sophisticated customers

Industry/Entity Type

Legal

Number of Pages Required

1 page

Requirements
Nice to have
• For a main background, tech type images to do with high powered boardrooms, computers, graphs, numbers, high tech manufacturing lines etc. Also, I tend to like blues and light greys, and uploaded a file today that shows my generally preferred layout, which a few of you have been getting close to.
Should not have
• Any mention of 'Personal Injury,' backgrounds that include books, or buildings with roman columns. Page should not be in dark colors or harsh on the eyes.

```html
<!DOCTYPE html>
<html lang="en">
<head>
<meta charset="utf-8">
<title>Dorvant Law Firm — Home</title>
<link href="https://fonts.googleapis.com/css2?family=Merriweather:wght@400;700&family=Poppins:wght@400;500&display=swap" rel="stylesheet">
<style>
:root{
  --bg:#eef2f6;
  --bg-band:#e2e9f0;
  --panel:#ffffff;
  --panel-2:#f3f6f9;
  --tile:#2d6190;
  --cyan:#18a6d4;
  --blue:#1d6fa5;
  --navy:#14294a;
  --red:#c8232a;
  --white:#ffffff;
  --text:#3a4553;
  --muted:#6b7685;
  --line:#c9d3de;
}
*{box-sizing:border-box;margin:0;padding:0}
html,body{width:1200px;height:4555px;overflow:hidden}
body{background:var(--bg);color:var(--text);font-family:"Merriweather",Georgia,serif;position:relative}
.abs{position:absolute}
.serif-h{font-family:"Merriweather",Georgia,serif;color:var(--navy);font-weight:700}
.btn{position:absolute;display:flex;align-items:center;gap:10px;padding:0 16px;height:40px;border-radius:8px;font-size:14px;font-weight:700;color:var(--navy);background:var(--white);font-family:"Merriweather",serif;white-space:nowrap}
.btn--cyan{border:2px solid var(--cyan)}
.btn--red{border:2px solid var(--red)}
.btn svg{width:15px;height:15px;fill:var(--navy)}
.ph{position:absolute}

/* top bar */
.topbar{top:0;left:0;width:1200px;height:72px;background:var(--white)}
.topbar__item{position:absolute;top:23px;display:flex;align-items:center;gap:8px;font-size:9.5px;color:var(--navy);font-weight:700;white-space:nowrap}
.topbar__item svg{width:18px;height:18px;stroke:var(--navy);fill:none;stroke-width:1.6;flex:none}
.logo-box{position:absolute;left:535px;top:0;width:122px;height:64px;background:#fff;border:1px solid var(--line);border-top:none;display:flex;align-items:center;justify-content:center;gap:6px}
.logo-box__mark{width:20px;height:20px;background:var(--navy)}
.logo-box__name{font-size:10px;color:var(--navy);font-weight:400;letter-spacing:1px;line-height:1.25}
.social{position:absolute;top:22px;left:888px;display:flex;gap:6px}
.social span{width:18px;height:18px;border-radius:50%;background:var(--navy)}
.social span.alt{background:var(--cyan)}

/* nav */
.nav{top:72px;left:0;width:1200px;height:38px;background:#dde6ef;display:flex;justify-content:center;gap:48px;font-family:"Poppins",sans-serif;font-size:14px;padding-top:9px}
.nav a{color:var(--navy);text-decoration:none;height:28px}
.nav a.active{color:var(--blue);border-bottom:2px solid var(--cyan)}

/* hero */
.hero{top:110px;left:0;width:1200px;height:452px;background:linear-gradient(90deg,#f4f7fa 0%,#e6edf4 55%,#cfdcea 80%,#e9eef4 100%)}
.hero__title{top:245px;left:173px;width:520px;font-size:33px;line-height:44px}
.hero__lede{top:342px;left:173px;width:520px;font-size:12px;line-height:16px;color:var(--text)}

/* case evaluation */
.case-band{top:562px;left:0;width:1200px;height:595px;background:var(--bg-band)}
.case-card{top:627px;left:173px;width:852px;height:472px;background:var(--panel);box-shadow:0 4px 18px rgba(20,41,74,.08)}
.case-card h2{position:absolute;top:30px;width:100%;text-align:center;font-size:23px;color:var(--navy);font-weight:400}
.case-card p.sub{position:absolute;top:69px;width:100%;text-align:center;font-size:11px}
.field{position:absolute;border:1px solid #aab6c4;border-radius:3px;font-family:"Poppins",sans-serif;font-size:12px;color:var(--muted);padding:18px 18px;background:#fbfcfd}
.case-card .legal{position:absolute;top:355px;width:100%;text-align:center;font-size:11px}
.case-card .legal u{color:var(--navy)}

/* about */
.about__frame{top:1223px;left:154px;width:373px;height:367px;background:var(--blue)}
.about__title{top:1225px;left:575px;width:460px;font-size:21px;line-height:28px}
.about__copy{position:absolute;left:575px;width:450px;font-size:11.5px;line-height:18.7px}
.badge{top:1553px;left:575px;width:450px;height:56px;background:var(--panel);display:flex;align-items:center;gap:12px;padding:0 10px}
.badge__shape{width:130px;height:40px;background:#f6e4e5;border:1px solid var(--red);flex:none}
.badge__text{font-size:9.5px;line-height:12px}

/* practice areas */
.pa__title{top:1756px;left:0;width:1200px;text-align:center;font-size:21px}
.tile{position:absolute;width:170px;background:var(--tile);display:flex;flex-direction:column;align-items:center;justify-content:center;gap:14px;text-align:center;color:var(--white);font-size:15px;font-weight:400;line-height:19px}
.tile svg{width:56px;height:56px;fill:none;stroke:var(--white);stroke-width:2.5}

/* have a case */
.cta-box{top:2391px;left:507px;width:518px;height:221px;border:7px solid var(--cyan);background:rgba(255,255,255,.97)}
.cta-box__thumb{top:0;left:0;width:150px;height:100%}
.cta-box h3{position:absolute;top:30px;left:170px;font-size:21px;color:var(--navy)}
.cta-box p{position:absolute;top:70px;left:170px;width:310px;font-size:11.5px;line-height:18px}

/* testimonials */
.testi{top:2675px;left:0;width:1200px;height:534px;background:linear-gradient(180deg,#e4ebf2,#f1f4f8)}
.testi__title{top:2746px;width:1200px;text-align:center;font-size:21px;font-weight:400;letter-spacing:.5px}
.testi__box{top:2855px;left:173px;width:852px;height:297px;border:2px solid #9fb0c3;border-top:none}
.testi__cap{top:2855px;height:2px;background:#9fb0c3}
.testi__quote{top:2920px;left:288px;width:655px;text-align:center;font-size:11.5px;line-height:18.5px}
.testi__name{top:3083px;left:0;width:1200px;text-align:center;font-size:16px;color:var(--red);font-weight:700}
.testi__role{top:3106px;left:0;width:1200px;text-align:center;font-size:11px;color:var(--navy)}
.quote-mark{font-size:70px;color:var(--navy);font-weight:700;line-height:1}
.pager{top:3125px;left:568px;display:flex;gap:2px}
.pager span{background:var(--red);color:#fff;font-size:7px;padding:1px 5px;font-family:"Poppins",sans-serif}

/* news */
.news__title{top:3280px;left:173px;font-size:21px;font-weight:400}
.news-card{position:absolute;top:3340px;width:283px;height:415px;background:var(--panel)}
.news-card__img{position:absolute;top:0;left:0;width:100%;height:253px}
.news-card__meta{position:absolute;top:267px;left:23px;font-size:11px;display:flex;gap:40px;white-space:nowrap}
.news-card h4{position:absolute;top:290px;left:23px;width:245px;font-size:13px;line-height:18px;color:var(--navy)}
.news-card p{position:absolute;top:340px;left:23px;width:245px;font-size:11px;line-height:18px}
.news-card .more{position:absolute;top:383px;left:23px;font-size:12px;font-weight:700;color:var(--navy)}

/* work together */
.work{top:3882px;left:173px;width:852px;height:270px;background:linear-gradient(90deg,#dbe5ef,#f4f7fa)}
.work h3{position:absolute;top:65px;left:477px;font-size:22px;font-weight:400;color:var(--navy);letter-spacing:.5px}
.work p{position:absolute;top:108px;left:477px;width:310px;font-size:11.5px;line-height:18px}

/* footer */
.footer{top:4214px;left:0;width:1200px;height:341px;background:#dde5ee}
.footer__logo{top:4282px;left:515px;display:flex;align-items:center;gap:10px}
.footer__logo i{width:38px;height:38px;background:var(--navy);display:block}
.footer__logo span{font-size:16px;color:var(--navy);letter-spacing:4px;line-height:20px}
.footer__about{top:4348px;left:260px;width:680px;text-align:center;font-size:11.5px;line-height:18px}
.footer__offices{top:4418px;left:223px;font-size:11.5px;line-height:23px}
.footer__offices b{color:var(--navy)}
.footer__phone{top:4418px;left:853px;font-size:11.5px;line-height:23px;color:var(--navy)}
.footer__phone span{color:var(--blue)}
.footer__copy{top:4525px;left:0;width:1200px;text-align:center;font-size:11.5px}
</style>
</head>
<body>

<header class="abs topbar">
  <div class="topbar__item" style="left:173px"><svg viewBox="0 0 20 20"><circle cx="10" cy="10" r="9"/><circle cx="10" cy="8" r="2.5"/><path d="M10 15c-3-3.5-4-5.5-4-7a4 4 0 0 1 8 0c0 1.5-1 3.5-4 7z"/></svg>18 Harbour Ln, Fernvale, ON L0S 2K4</div>
  <div class="topbar__item" style="left:420px"><svg viewBox="0 0 20 20"><circle cx="10" cy="10" r="9"/><path d="M7 6l2 2-1 1.5c.8 1.5 1.8 2.5 3 3l1.5-1 2 2-1.5 1.5C9.5 14.5 5.5 10.5 5.5 7.5z"/></svg>555.010.4477</div>
  <div class="logo-box"><span class="logo-box__mark"></span><span class="logo-box__name">DORVANT<br>LAW FIRM</span></div>
  <div class="topbar__item" style="left:690px"><svg viewBox="0 0 20 20"><circle cx="10" cy="10" r="9"/><rect x="5" y="6.5" width="10" height="7"/><path d="M5 6.5l5 4 5-4"/></svg>adrian@dorvantlegal.ca</div>
  <div class="social"><span></span><span class="alt"></span><span></span><span></span><span></span><span></span></div>
</header>

<nav class="abs nav">
  <a class="active">Practice Areas</a><a>About</a><a>News or News Articles</a><a>Resources or Legal Resources</a><a>Contact</a>
</nav>

<section class="abs hero"></section>
<div class="ph" role="img" aria-label="Photo of brass scales of justice and a gavel" style="top:415px;left:0;width:170px;height:147px;background:radial-gradient(ellipse at 45% 70%,#c9a85a 0%,#d9cfb8 45%,transparent 75%)"></div>
<div class="ph" role="img" aria-label="Portrait of the lead lawyer in a dark suit" style="top:150px;left:733px;width:283px;height:412px;background:linear-gradient(180deg,#c6d3e1 0%,#7f91a8 45%,#3d4b60 100%)"></div>
<h1 class="abs serif-h hero__title">Winning.My clients depend on me for it.Shouldn't you?</h1>
<p class="abs hero__lede">I've handled cases involving complex business disputes, legal and medical malpractice, insurance claim denials and high-stakes commercial contracts.</p>
<a class="btn btn--cyan" style="top:393px;left:173px;width:135px"><svg viewBox="0 0 16 16"><rect x="2" y="2" width="12" height="12" rx="1"/></svg>Read More</a>
<a class="btn btn--red" style="top:393px;left:324px;width:158px"><svg viewBox="0 0 16 16"><rect x="1" y="4" width="10" height="8" rx="1"/><path d="M11 7l4-2v6l-4-2z"/></svg>Video Library</a>

<section class="abs case-band"></section>
<div class="ph" role="img" aria-label="Line drawing of Lady Justice" style="top:900px;left:1030px;width:170px;height:350px;background:linear-gradient(180deg,rgba(29,111,165,.10),rgba(29,111,165,.03))"></div>
<form class="abs case-card">
  <h2>CASE EVALUATION</h2>
  <p class="sub">Fill out this form to schedule your initial consult with our lawyers.</p>
  <div class="field" style="top:115px;left:62px;width:355px;height:54px">Name</div>
  <div class="field" style="top:115px;left:437px;width:355px;height:54px">Phone</div>
  <div class="field" style="top:187px;left:62px;width:730px;height:54px">Email</div>
  <div class="field" style="top:260px;left:62px;width:730px;height:78px">Message</div>
  <p class="legal">* By using this site and/or submitting this form, I agree to the <u>Privacy Policy</u> and <u>Terms of Use</u>.</p>
  <a class="btn btn--red" style="top:403px;left:373px;height:36px;width:108px"><svg viewBox="0 0 16 16"><rect x="2" y="2" width="12" height="12" rx="1"/></svg>Submit</a>
</form>

<div class="abs about__frame"></div>
<div class="ph" role="img" aria-label="Studio portrait of the lead lawyer with red tie" style="top:1246px;left:173px;width:372px;height:366px;background:linear-gradient(180deg,#e4e6ea 0%,#c8ccd3 55%,#4a5362 100%)"></div>
<h2 class="abs serif-h about__title">Your Experienced Toronto and Hamilton Lawyers – Getting the Results That Matter</h2>
<p class="about__copy" style="top:1291px">Dorvant Law Firm is a boutique litigation firm with law offices in Toronto and Hamilton. We concentrate our legal practice on complex business litigation, professional negligence (malpractice) claims, commercial contracts, and insurance coverage disputes. We take an innovative approach to our client's legal problems, and are guided by the philosophy that our job is to get results.</p>
<p class="about__copy" style="top:1403px">The lawyers at Dorvant Law Firm have the reputation for vigorously representing their clients' interests and competing hard to obtain the best possible results. With experience at all stages of legal disputes, the lawyers at Dorvant Law Firm are equally at home negotiating in a boardroom or presenting a case at trial. We hope that you take the time to explore our website to find out how our record of excellence, expertise and many years of experience can assist you.</p>
<div class="abs badge"><span class="badge__shape"></span><span class="badge__text">An excellent rating for a lawyer with some experience. This rating indicates the attorney is widely respected by their peers for high professional achievement and ethical standards.</span></div>

<h2 class="abs serif-h pa__title">Dorvant Law Firm Practice Areas</h2>
<div class="ph" role="img" aria-label="Line drawing of Lady Justice" style="top:1880px;left:0;width:180px;height:410px;background:linear-gradient(180deg,rgba(29,111,165,.10),rgba(29,111,165,.03))"></div>
<div class="ph" role="img" aria-label="Video still of a handshake over a desk with scales and gavel" style="top:1788px;left:491px;width:536px;height:361px;background:linear-gradient(135deg,#dfe6ee 0%,#a9b8c8 40%,#eef0f2 70%,#c2a878 100%)"></div>
<svg class="abs" style="top:1918px;left:710px" width="100" height="100" viewBox="0 0 100 100"><circle cx="50" cy="50" r="44" fill="none" stroke="#18a6d4" stroke-width="7"/><path d="M40 30v40l32-20z" fill="#18a6d4"/></svg>
<div class="tile" style="top:1832px;left:173px;height:184px"><svg viewBox="0 0 56 56"><path d="M8 26L28 8l20 18M14 22v26h28V22M22 48V34h12v14"/></svg>BUSINESS<br>LITIGATION</div>
<div class="tile" style="top:1881px;left:361px;height:184px"><svg viewBox="0 0 56 56"><rect x="10" y="8" width="28" height="38" rx="3"/><path d="M16 18h16M16 26h10"/><circle cx="40" cy="40" r="10"/><path d="M35 40l4 4 6-7"/></svg>INSURANCE</div>
<div class="tile" style="top:2035px;left:173px;height:184px"><svg viewBox="0 0 56 56"><rect x="12" y="6" width="32" height="42" rx="2"/><path d="M18 16h20M18 24h20M18 32h12"/><path d="M30 42l4 4 8-9"/></svg>COMMERCIAL<br>CONTRACTS</div>
<div class="tile" style="top:2083px;left:361px;height:184px"><svg viewBox="0 0 56 56"><circle cx="28" cy="24" r="18"/><path d="M18 26l6-6 4 3 4-3 6 6-6 5-8-1z"/><path d="M20 42l-4 10 8-4M36 42l4 10-8-4"/></svg>PROFESSIONAL<br>NEGLIGENCE</div>

<div class="ph" role="img" aria-label="Photo of a lawyer handing a folder across a desk with a laptop and gavel" style="top:2325px;left:0;width:659px;height:350px;background:linear-gradient(120deg,#f1f2f3 0%,#cfd5dc 35%,#b59a72 60%,#8a7a6a 100%)"></div>
<div class="abs cta-box">
  <div class="ph cta-box__thumb" role="img" aria-label="Detail of the same desk photo" style="background:linear-gradient(90deg,#9a8a76,#d2c6b6)"></div>
  <h3>Have A Case? Lets Evaluate It.</h3>
  <p>We take an innovative approach to our client's legal problems, and are guided by the philosophy that our job is to get results.</p>
  <a class="btn btn--cyan" style="top:130px;left:170px;width:228px;font-weight:400"><svg viewBox="0 0 16 16"><rect x="2" y="2" width="10" height="12" rx="1"/></svg>Lets Evaluate Your Case</a>
</div>

<section class="abs testi"></section>
<h2 class="abs serif-h testi__title">WHAT OUR CLIENTS ARE SAYING</h2>
<div class="abs testi__box"></div>
<div class="abs testi__cap" style="left:173px;width:264px"></div>
<div class="abs testi__cap" style="left:761px;width:264px"></div>
<div class="ph" role="img" aria-label="Photo of the reviewing couple" style="top:2804px;left:557px;width:88px;height:88px;border-radius:50%;background:radial-gradient(circle,#c9a98a,#7a6454)"></div>
<span class="abs quote-mark" style="top:2885px;left:238px">“</span>
<span class="abs quote-mark" style="top:3030px;left:912px">”</span>
<p class="abs testi__quote">We highly recommend Adrian Keller, he truly comes as advertised. My Wife and I were caught up in a long drawn out civil action over an asset purchase agreement that lasted almost 5 years. We had previously changed lawyers 3 times and were in a dire situation less than 2 months from trial. We needed someone who cared about their clients, was ethical, knowledgeable, dedicated, and affordable. After endless searching we found Dorvant Law Firm, contacted him, and were amazed by his dedication to our file. He was well informed within a few weeks and did more work in 6 weeks than the other firms did over 5 years. He contacted all witnesses, studied the transcripts, documents, talked with us constantly, and made excellent use of all resources available...</p>
<div class="abs testi__name">Mark &amp; Ellen Varga</div>
<div class="abs testi__role">Business Litigation Clients</div>
<div class="abs pager"><span>‹ Prev</span><span>Next ›</span></div>

<h2 class="abs serif-h news__title">LATEST NEWS</h2>
<a class="btn btn--red" style="top:3274px;left:838px;width:187px;font-weight:400"><svg viewBox="0 0 16 16"><rect x="2" y="3" width="12" height="10"/></svg>More Media News</a>
<article class="news-card" style="left:173px">
  <div class="ph news-card__img" role="img" aria-label="Photo of a lawyer writing at a desk" style="background:linear-gradient(180deg,#c4ceda,#8d9bad)"></div>
  <div class="news-card__meta"><span>Adrian Keller</span><span>May 30th, 2022</span></div>
  <h4>How to Get the Most out of an Initial Consultation with a Lawyer</h4>
  <p>How to Get the Most out of an Initial Consultation with a Lawyer If you're</p>
  <span class="more">View More →</span>
</article>
<article class="news-card" style="left:457px">
  <div class="ph news-card__img" role="img" aria-label="Photo of a pen signing a document" style="background:linear-gradient(180deg,#cdd5df,#94a2b3)"></div>
  <div class="news-card__meta"><span>Adrian Keller</span><span>November 2nd, 2021</span></div>
  <h4>How to Protect Yourself During Construction/Renovations</h4>
  <p>Construction and renovation expenses can be substantial, often in excess</p>
  <span class="more">View More →</span>
</article>
<article class="news-card" style="left:741px">
  <div class="ph news-card__img" role="img" aria-label="Photo of a laptop on an office desk" style="background:linear-gradient(180deg,#c0cbd8,#8696a9)"></div>
  <div class="news-card__meta"><span>Adrian Keller</span><span>May 30th, 2022</span></div>
  <h4>How to Protect Yourself During Construction/Renovations</h4>
  <p>How to Get the Most out of an Initial Consultation with a Lawyer If you're</p>
  <span class="more">View More →</span>
</article>

<div class="abs work">
  <div class="ph" role="img" aria-label="Portrait of the lead lawyer in a blue shirt and grey suit" style="top:10px;left:95px;width:210px;height:260px;background:linear-gradient(180deg,#c9d4e0 0%,#5f7698 55%,#3a4760 100%)"></div>
  <h3>LET'S WORK TOGETHER</h3>
  <p>We take an innovative approach to our client's legal problems, and are guided by the philosophy that our job is to get results.</p>
  <a class="btn btn--red" style="top:172px;left:477px;width:228px;font-weight:400"><svg viewBox="0 0 16 16"><rect x="2" y="2" width="10" height="12" rx="1"/></svg>Lets Evaluate Your Case</a>
</div>

<footer class="abs footer"></footer>
<div class="abs footer__logo"><i></i><span>DORVANT<br>LAW FIRM</span></div>
<p class="abs footer__about">Dorvant Law Firm is a boutique law office concentrating in Complex Business Litigation, Professional Negligence, Commercial Contracts, and Insurance Coverage Disputes. Our innovative and pugnacious approach gets results for our clients in the Greater Toronto Area. HST #100200300RT0001</p>
<svg class="abs" style="top:4420px;left:175px" width="28" height="34" viewBox="0 0 28 34"><path d="M14 32C5 21 3 16 3 12a11 11 0 0 1 22 0c0 4-2 9-11 20z" fill="none" stroke="#1d6fa5" stroke-width="4"/><circle cx="14" cy="12" r="4" fill="#1d6fa5"/></svg>
<div class="abs footer__offices">
  <div><b>Hamilton Office:</b> 42 Bayview Road, Ground Floor Hamilton, ON L8N 0A1</div>
  <div><b>Toronto Office:</b> 250 Front Street W #1200, Toronto, ON M5V 0A2</div>
  <div><b>Niagara Office:</b> 18 Harbour Ln, Fernvale, ON L0S 2K4 <u>Sitemap</u></div>
</div>
<svg class="abs" style="top:4418px;left:803px" width="32" height="32" viewBox="0 0 32 32"><path d="M8 4l6 6-3 4c2 4 4 6 8 8l4-3 6 6-4 4C14 29 3 18 4 8z" fill="none" stroke="#1d6fa5" stroke-width="3"/></svg>
<div class="abs footer__phone">GTA – HAMILTON – NIAGARA<br><span>555.010.4477</span></div>
<div class="abs footer__copy">© 2023 Dorvant Law Firm. All Rights Reserved.</div>

</body>
</html>
```